Broadcaster,Conference Host,Facilitator

Looking for a business card and logo to create the Grant Felber brand .. Something with a slant towards radio and conference speaking
I like the idea of classic black white or grey but open to suggestions

Target Market(s)

Corporates

Industry/Entity Type

Business

Contact Information for Business Card

Grant Felber
Email : Grant.Felber@quorvamail.co.uk
Mobile : +44 7700 382046
Twitter : @Grantfelber

Font styles to use
Serif
Decorative
Script

Requirements
Must have
• Feel classy and dynamic
Should not have
• Cartoons

```html
<!DOCTYPE html>
<html lang="en">
<head>
<meta charset="utf-8">
<title>Grant Felber Voice – Business Card</title>
<link rel="stylesheet" href="https://fonts.googleapis.com/css2?family=Jost:wght@400&family=Open+Sans:wght@400&display=swap">
<style>
  :root {
    --backdrop: #e8e5e1;
    --card: #ffffff;
    --ink: #111111;
    --rule: #333333;
  }
  html, body {
    margin: 0;
    padding: 0;
    width: 1200px;
    height: 1000px;
    overflow: hidden;
    background: var(--backdrop);
  }
  .canvas {
    position: relative;
    width: 1200px;
    height: 1000px;
  }
  .card {
    position: absolute;
    left: 265px;
    width: 665px;
    height: 397px;
    background: var(--card);
    border-radius: 22px;
    color: var(--ink);
  }
  .card--front { top: 73px; }
  .card--back { top: 532px; }

  .emblem {
    position: absolute;
    left: 266px;
    top: 30px;
    width: 134px;
    height: 134px;
  }
  .wordmark {
    position: absolute;
    left: 0;
    right: 0;
    top: 172px;
    text-align: center;
    font-family: "Jost", sans-serif;
    font-weight: 400;
  }
  .wordmark__name {
    font-size: 47px;
    line-height: 52px;
    letter-spacing: 0.5px;
    text-transform: uppercase;
  }
  .wordmark__tag {
    display: flex;
    justify-content: center;
    align-items: center;
    gap: 14px;
    margin-top: 0;
    font-size: 22px;
    line-height: 26px;
    letter-spacing: 7px;
    text-transform: uppercase;
  }
  .wordmark__tag .rule {
    width: 78px;
    height: 1.5px;
    background: var(--rule);
  }
  .wordmark__tag .label { padding-left: 7px; }

  .contact {
    position: absolute;
    left: 0;
    right: 0;
    top: 287px;
    font-family: "Open Sans", sans-serif;
    font-size: 16px;
    text-align: center;
  }
  .contact__icon {
    display: block;
    margin: 0 auto;
    width: 20px;
    height: 20px;
  }
  .contact__email { margin-top: 2px; line-height: 24px; }
  .contact__row {
    display: flex;
    justify-content: center;
    align-items: center;
    gap: 8px;
    margin-top: 9px;
    line-height: 24px;
  }
  .contact__row svg { width: 20px; height: 20px; display: block; }
  .contact__divider {
    width: 1px;
    height: 26px;
    background: var(--rule);
    margin: 0 4px;
  }
</style>
</head>
<body>
<div class="canvas">

  <section class="card card--front">
    <svg class="emblem" viewBox="0 0 134 134" role="img" aria-label="Logo emblem: vintage microphone in a black circle">
      <circle cx="67" cy="67" r="66" fill="var(--ink)"/>
      <circle cx="67" cy="67" r="60" fill="none" stroke="#ffffff" stroke-width="2"/>
    </svg>
    <div class="wordmark">
      <div class="wordmark__name">Grant Felber</div>
      <div class="wordmark__tag"><span class="rule"></span><span class="label">Voice</span><span class="rule"></span></div>
    </div>
    <div class="contact">
      <svg class="contact__icon" viewBox="0 0 20 20" aria-hidden="true">
        <circle cx="10" cy="10" r="9" fill="none" stroke="var(--ink)" stroke-width="1.5"/>
        <rect x="5" y="6.5" width="10" height="7" fill="var(--ink)"/>
        <path d="M5 6.5 L10 10.5 L15 6.5" fill="none" stroke="#fff" stroke-width="1"/>
      </svg>
      <div class="contact__email">grant.felber@quorvamail.co.uk</div>
      <div class="contact__row">
        <span>+44 7700 382046</span>
        <svg viewBox="0 0 20 20" aria-hidden="true">
          <circle cx="10" cy="10" r="9" fill="none" stroke="var(--ink)" stroke-width="1.5"/>
          <path d="M5 8.5 Q10 5 15 8.5 L14 10 L12 9.5 L11.5 8.5 H8.5 L8 9.5 L6 10 Z" fill="var(--ink)"/>
          <rect x="6.5" y="10.5" width="7" height="4" rx="1" fill="var(--ink)"/>
        </svg>
        <span class="contact__divider"></span>
        <svg viewBox="0 0 20 20" aria-hidden="true">
          <circle cx="10" cy="10" r="9" fill="none" stroke="var(--ink)" stroke-width="1.5"/>
        </svg>
        <span>@Grantfelber</span>
      </div>
    </div>
  </section>

  <section class="card card--back">
    <svg class="emblem" viewBox="0 0 134 134" role="img" aria-label="Logo emblem: vintage microphone in a black circle">
      <circle cx="67" cy="67" r="66" fill="var(--ink)"/>
      <circle cx="67" cy="67" r="60" fill="none" stroke="#ffffff" stroke-width="2"/>
    </svg>
    <div class="wordmark">
      <div class="wordmark__name">Grant Felber</div>
      <div class="wordmark__tag"><span class="rule"></span><span class="label">Voice</span><span class="rule"></span></div>
    </div>
    <div class="contact">
      <svg class="contact__icon" viewBox="0 0 20 20" aria-hidden="true">
        <circle cx="10" cy="10" r="9" fill="none" stroke="var(--ink)" stroke-width="1.5"/>
        <rect x="5" y="6.5" width="10" height="7" fill="var(--ink)"/>
        <path d="M5 6.5 L10 10.5 L15 6.5" fill="none" stroke="#fff" stroke-width="1"/>
      </svg>
      <div class="contact__email">grant.felber@quorvamail.co.uk</div>
      <div class="contact__row">
        <span>+44 7700 382046</span>
        <svg viewBox="0 0 20 20" aria-hidden="true">
          <circle cx="10" cy="10" r="9" fill="none" stroke="var(--ink)" stroke-width="1.5"/>
          <path d="M5 8.5 Q10 5 15 8.5 L14 10 L12 9.5 L11.5 8.5 H8.5 L8 9.5 L6 10 Z" fill="var(--ink)"/>
          <rect x="6.5" y="10.5" width="7" height="4" rx="1" fill="var(--ink)"/>
        </svg>
        <span class="contact__divider"></span>
        <svg viewBox="0 0 20 20" aria-hidden="true">
          <circle cx="10" cy="10" r="9" fill="none" stroke="var(--ink)" stroke-width="1.5"/>
        </svg>
        <span>@Grantfelber</span>
      </div>
    </div>
  </section>

</div>
</body>
</html>
```